arts & crafts

I collect old plates & make them into serving plates for cakes, afternoon teas, special occasions, weddings, parties, bridal showers. cake competitions, displays in bakeries.

Contact Information for Business Card

Tulips Turn Gold
Bringing the old back to new
Ph 0417283956
info@ tulipsturngold.com.au
www.tulipsturngold.com.au
pagebook
Craftlo

```html
<!DOCTYPE html>
<html lang="en">
<head>
<meta charset="UTF-8">
<title>Tulips Turn Gold – Business Card</title>
<link href="https://fonts.googleapis.com/css2?family=Quicksand:wght@500;600;700&display=swap" rel="stylesheet">
<style>
  :root {
    --backdrop: #e9e9e9;
    --paper: #f7f7f5;
    --teal: #1ba3b5;
    --red: #e0323f;
    --charcoal: #2a2624;
    --divider: #1b1817;
    --divider-light: #3a3532;
    --white: #ffffff;
  }
  * { box-sizing: border-box; margin: 0; padding: 0; }
  html, body {
    width: 1200px;
    height: 800px;
    overflow: hidden;
    background: var(--backdrop);
  }
  .canvas {
    position: relative;
    width: 1200px;
    height: 800px;
  }
  .card {
    position: absolute;
    left: 430px;
    top: 110px;
    width: 340px;
    height: 580px;
    background: var(--paper);
    box-shadow: 0 6px 18px rgba(0,0,0,0.12);
    overflow: hidden;
    font-family: "Quicksand", sans-serif;
  }
  .tab {
    position: absolute;
    height: 11px;
    background: var(--teal);
  }
  .tab--left { left: 0; top: 0; width: 64px; }
  .tab--right { right: 0; top: 22px; width: 70px; }

  .brand {
    position: absolute;
    left: 0;
    top: 0;
    width: 100%;
    height: 190px;
    text-align: center;
  }
  .brand__mark {
    position: absolute;
    left: 50%;
    top: 36px;
    width: 58px;
    height: 58px;
    margin-left: -29px;
    border-radius: 50%;
    background: var(--teal);
  }
  .brand__name {
    position: absolute;
    left: 0;
    right: 0;
    top: 112px;
    font-weight: 700;
    font-size: 31px;
    color: var(--red);
    letter-spacing: 0.5px;
  }

  .contact {
    position: absolute;
    left: 0;
    top: 190px;
    width: 100%;
    height: 390px;
    background: var(--charcoal);
    list-style: none;
  }
  .contact__row {
    display: flex;
    align-items: center;
    height: 97.5px;
    padding-left: 30px;
    border-bottom: 2px solid var(--divider);
    box-shadow: inset 0 -1px 0 var(--divider-light);
    color: var(--white);
    font-size: 17px;
    font-weight: 500;
    line-height: 1.3;
    letter-spacing: 0.3px;
  }
  .contact__row:last-child { border-bottom: none; box-shadow: none; }
  .contact__icon {
    flex: none;
    width: 44px;
    height: 44px;
    margin-right: 22px;
  }
  .person__name {
    font-weight: 700;
    font-size: 19px;
    letter-spacing: 0.8px;
    line-height: 1;
  }
  .person__role {
    color: var(--red);
    font-weight: 700;
    font-size: 13px;
    letter-spacing: 0.8px;
  }
</style>
</head>
<body>
<main class="canvas">
  <article class="card">
    <span class="tab tab--left"></span>
    <span class="tab tab--right"></span>

    <header class="brand">
      <span class="brand__mark"></span>
      <h1 class="brand__name">Tulips Turn Gold</h1>
    </header>

    <ul class="contact">
      <li class="contact__row">
        <svg class="contact__icon" viewBox="0 0 44 44" aria-hidden="true">
          <circle cx="22" cy="22" r="20.5" fill="none" stroke="var(--red)" stroke-width="2"/>
          <circle cx="22" cy="17" r="6" fill="var(--white)"/>
          <path d="M11 32 q0 -8 11 -8 q11 0 11 8 z" fill="var(--white)"/>
        </svg>
        <div>
          <p class="person__name">JANE DOE</p>
          <p class="person__role">DECORATOR</p>
        </div>
      </li>
      <li class="contact__row">
        <svg class="contact__icon" viewBox="0 0 44 44" aria-hidden="true">
          <circle cx="22" cy="22" r="20.5" fill="none" stroke="var(--red)" stroke-width="2"/>
          <path d="M12 18 q10 -7 20 0 l-1.5 3 h-4 v-3 h-9 v3 h-4 z" fill="var(--white)"/>
          <rect x="14" y="22" width="16" height="9" rx="1.5" fill="var(--white)"/>
          <circle cx="22" cy="26.5" r="2.3" fill="var(--charcoal)"/>
        </svg>
        <p>0417283956</p>
      </li>
      <li class="contact__row">
        <svg class="contact__icon" viewBox="0 0 44 44" aria-hidden="true">
          <circle cx="22" cy="22" r="20.5" fill="none" stroke="var(--red)" stroke-width="2"/>
          <g fill="none" stroke="var(--white)" stroke-width="1.6">
            <circle cx="22" cy="22" r="10"/>
            <ellipse cx="22" cy="22" rx="4.5" ry="10"/>
            <line x1="12" y1="22" x2="32" y2="22"/>
            <line x1="13.5" y1="17" x2="30.5" y2="17"/>
            <line x1="13.5" y1="27" x2="30.5" y2="27"/>
          </g>
        </svg>
        <p>info@tulipsturngold.com.au<br>www.tulipsturngold.com.au</p>
      </li>
      <li class="contact__row">
        <svg class="contact__icon" viewBox="0 0 44 44" aria-hidden="true">
          <circle cx="22" cy="22" r="20.5" fill="none" stroke="var(--red)" stroke-width="2"/>
        </svg>
        <p>/pagebook<br>/craftlo</p>
      </li>
    </ul>
  </article>
</main>
</body>
</html>
```